Investment Real Estate Firm Needs Template to Showcase properties

We're a firm that sells $1M-$20M Dollar properties. We need a very professional template to be able to insert our information, pictures, and data into it. The data is mostly send via email in PDF and/or printed out. Here's the templates we need using OUR Logo and colors. Name of Company: Halden Capital Partners

1.)Cover Page Template: I've attached a example but we would like our own original cover page that looks cool and has spot for property photo
2.)Table of Contents Template: I've attached some cool original ideas that we like. Obviously would love our own
3.)Beginning of Section Template: Basically a page letting you know what section you're about ready to start.
4.) Content/Data Template: This is the template where all data will be inserted. So basically just bordering and very minimal space taken up to allow for content to be added
5.) Back Page/Last Page Template: This will be the last page of the presentation or showcase. I can also use this page to insert disclaimers and confidentiality language.

Target Market(s)

This only goes to a targeted personal client base

Industry/Entity Type

Real Estate

Font styles to use
Serif

Requirements
Must have
• - Cover Page, Contents Page, Section Page, Content Page, Back Page
• - Use our Logo. Attached
• - Use Our color scheme
• - Professional Look but some original ideas ;)
• - Abbility for me to edit and Drop in content
Nice to have
• Some Creativity in bordering and maybe carry over the section identity somehow within the border.
• A Extremely light but noticeable transparent "HCP" Logo Only on content pages in background centered " See attached

```html
<!DOCTYPE html>
<html lang="en">
<head>
<meta charset="utf-8">
<title>Halden Capital Partners — Presentation Template</title>
<link href="https://fonts.googleapis.com/css2?family=Libre+Baskerville&family=Lato:wght@400;700&display=swap" rel="stylesheet">
<style>
:root{
  --gold:#c4b78f;
  --gold-dark:#a99b72;
  --ink:#111111;
  --band:#0a0a0a;
  --paper:#ffffff;
  --panel:rgba(40,40,40,.82);
  --muted:#8b8b8b;
  --line:#cfcfcf;
}
*{margin:0;padding:0;box-sizing:border-box}
html,body{width:850px;height:1200px;overflow:hidden;background:#9a9a9a}
body{font-family:"Lato",sans-serif;color:var(--ink)}
.deck{display:grid;grid-template-columns:424px 424px;grid-template-rows:repeat(5,239px);gap:1px 2px;width:850px;height:1200px;background:#9a9a9a}
.slide{position:relative;overflow:hidden;background:var(--paper)}
.serif{font-family:"Libre Baskerville",serif}

/* shared */
.title{position:absolute;font-family:"Libre Baskerville",serif;font-weight:400;line-height:1.3}
.title::before{content:"";position:absolute;left:0;top:-9px;width:24px;height:3px;background:var(--gold)}
.bullet-sq{display:inline-block;width:10px;height:10px;background:var(--gold);flex:none}
.small{font-size:6px;line-height:1.45}
.footer{position:absolute;left:0;right:0;bottom:0;height:25px;background:var(--band);display:flex;align-items:center;padding:0 14px}
.footer .mark{font-family:"Libre Baskerville",serif;color:#9a9a9a;font-size:11px;width:60px}
.footer .url{flex:1;text-align:center;color:#aaa;font-size:4.5px;letter-spacing:.2px}
.footer .page{width:60px;display:flex;justify-content:flex-end}
.footer .page span{width:13px;height:13px;background:var(--gold);color:#222;font-size:5.5px;display:flex;align-items:center;justify-content:center}
.photo{position:absolute}
.icon-box{position:absolute;width:46px;height:46px;background:var(--gold);display:flex;align-items:center;justify-content:center}

/* cover */
.cover{background:linear-gradient(160deg,#2b2b2b,#5b5b5b 45%,#1e1e1e)}
.cover .frame{position:absolute;left:56px;top:72px;width:312px;height:78px;border:2px solid var(--gold)}
.cover .logo{position:absolute;left:0;right:0;top:56px;text-align:center}
.cover .logo span{background:#4a4a4a;padding:0 10px;font-family:"Libre Baskerville",serif;color:#d8d8d8;font-size:24px}
.cover .name{position:absolute;left:56px;width:312px;top:96px;text-align:center;color:#e6e6e6;font-size:19px;font-family:"Libre Baskerville",serif;letter-spacing:.5px}
.cover .sub{position:absolute;left:80px;width:264px;top:121px;display:flex;align-items:center;gap:8px;color:#cfcfcf;font-size:8px;letter-spacing:5px;font-family:"Libre Baskerville",serif}
.cover .sub i{flex:1;height:1px;background:#bbb}
.cover .intro{position:absolute;left:56px;top:158px;width:310px;display:flex;gap:10px;color:#ccc}

/* toc */
.toc-list{position:absolute;left:36px;top:66px;list-style:none}
.toc-list li{display:flex;align-items:center;gap:16px;font-size:8px;height:23px}

/* icon-explanation */
.subject{position:absolute;width:66px;text-align:center}
.subject h4{font-family:"Libre Baskerville",serif;font-weight:400;font-size:10px;margin-bottom:6px}
.subject p{font-size:5px;line-height:1.45;color:#333}
.vdiv{position:absolute;width:1px;background:var(--line)}

/* numbered */
.num{position:absolute;color:var(--gold);font-size:12px;font-family:"Lato",sans-serif}
.num-text{position:absolute;color:#999;font-size:5px;line-height:1.4;width:72px}

/* dark slides */
.dark-bg{position:absolute;inset:0;background:linear-gradient(180deg,#9c9c9c,#5e5e5e 55%,#3a3a3a)}
.dark-panel{position:absolute;top:0;bottom:25px;background:var(--panel)}
.dark .title{color:#e4e4e4}
.contact-row{position:absolute;left:36px;display:flex;align-items:center;gap:12px;color:#ddd;font-size:7px;line-height:1.3}
.contact-row .ic{width:16px;height:16px;background:var(--gold);display:flex;align-items:center;justify-content:center;flex:none}
.legal p{color:#d2d2d2;font-size:5.2px;line-height:1.45;margin-bottom:6px}
</style>
</head>
<body>
<main class="deck">

  <!-- 1 Cover -->
  <section class="slide cover">
    <div class="photo" style="inset:0;background:linear-gradient(160deg,#262626,#6a6a6a 50%,#1c1c1c)" role="img" aria-label="Black and white photo looking up at glass office towers"></div>
    <div class="frame"></div>
    <div class="logo"><span>HCP</span></div>
    <div class="name">HALDEN CAPITAL</div>
    <div class="sub"><i></i>PARTNERS<i></i></div>
    <div class="intro"><span class="bullet-sq"></span><p class="small">Private holdings of distinction, presented with care. Each property in this portfolio has been selected for lasting value, strong location and discreet ownership. Review the details and contact our advisors to arrange a visit.</p></div>
  </section>

  <!-- 2 Table of contents -->
  <section class="slide">
    <h2 class="title" style="left:36px;top:26px;font-size:18px">Table Of Contents</h2>
    <ul class="toc-list">
      <li><span class="bullet-sq"></span>Property overview and location summary</li>
      <li><span class="bullet-sq"></span>Financial highlights and income analysis</li>
      <li><span class="bullet-sq"></span>Market comparables</li>
      <li><span class="bullet-sq"></span>Floor plans and site</li>
      <li><span class="bullet-sq"></span>Tenant profile and lease schedule overview</li>
      <li><span class="bullet-sq"></span>Contact details</li>
    </ul>
    <div class="photo" style="left:256px;top:0;width:89px;height:214px;background:linear-gradient(180deg,#d9dfe6,#a7aeb5 55%,#7d4a36)" role="img" aria-label="Photo of a high-rise office tower beside a brick building"></div>
    <div class="photo" style="left:345px;top:0;width:45px;height:214px;background:var(--gold)"></div>
    <footer class="footer"><span class="mark">HCP</span><span class="url">www.HaldenCapitalPartners.com</span><span class="page"><span>2</span></span></footer>
  </section>

  <!-- 3 Section header -->
  <section class="slide">
    <h2 class="title" style="left:36px;top:72px;font-size:19px;line-height:1.35">Section<br>Header<br>Slide</h2>
    <div style="position:absolute;left:36px;top:152px;width:150px;display:flex;gap:8px"><span class="bullet-sq"></span><p class="small">A short introduction to the section that follows in this presentation.</p></div>
    <div class="photo" style="left:210px;top:0;width:180px;height:214px;background:linear-gradient(180deg,#9ec3e4,#d7e4ee 45%,#7c7f84)" role="img" aria-label="Photo of a site manager holding a tablet overlooking a construction site"></div>
    <footer class="footer"><span class="mark">HCP</span><span class="url">www.HaldenCapitalPartners.com</span><span class="page"><span>3</span></span></footer>
  </section>

  <!-- 4 Content -->
  <section class="slide">
    <h2 class="title" style="left:36px;top:26px;font-size:18px">Content Slide</h2>
    <footer class="footer"><span class="mark">HCP</span><span class="url">www.HaldenCapitalPartners.com</span><span class="page"><span>4</span></span></footer>
  </section>

  <!-- 5 Features with photos -->
  <section class="slide">
    <div class="photo" style="left:36px;top:2px;width:172px;height:76px;background:linear-gradient(135deg,#3f7fb0,#d6dde3 50%,#3b6f8f)" role="img" aria-label="Photo of a modern glass facade with steel beams"></div>
    <div class="photo" style="left:214px;top:2px;width:172px;height:117px;background:linear-gradient(160deg,#e9e6dc,#9aa78a 45%,#b07a44)" role="img" aria-label="Photo of a bright atrium lobby with indoor trees"></div>
    <div class="photo" style="left:214px;top:126px;width:211px;height:86px;background:linear-gradient(90deg,#6e9aa4,#c3d6da 50%,#4c6f78)" role="img" aria-label="Photo of a glass curtain wall"></div>
    <h2 class="title" style="left:36px;top:110px;font-size:13px">Features With<br>Accompanying Photos</h2>
    <div style="position:absolute;left:36px;top:150px;width:160px;display:flex;gap:10px"><span class="bullet-sq"></span><p class="small">Highlight key features of the property here. Pair each point with a photo so clients can see finishes, common areas and the building exterior at a glance.</p></div>
    <footer class="footer"><span class="mark">HCP</span><span class="url">www.HaldenCapitalPartners.com</span><span class="page"><span>5</span></span></footer>
  </section>

  <!-- 6 Explanation with iconography -->
  <section class="slide">
    <h2 class="title" style="left:36px;top:78px;font-size:14px;line-height:1.4">Explanation<br>With<br>Iconography</h2>
    <div class="icon-box" style="left:171px;top:70px"><svg width="30" height="30" viewBox="0 0 30 30" fill="none" stroke="#111" stroke-width="2"><circle cx="15" cy="15" r="13"/><polyline points="7,19 12,12 17,17 23,9"/></svg></div>
    <div class="icon-box" style="left:251px;top:70px"><svg width="28" height="28" viewBox="0 0 28 28"><circle cx="14" cy="14" r="12" fill="#111"/><path d="M14 14 L14 2 A12 12 0 0 1 26 14 Z" fill="var(--gold)"/><path d="M15.5 12.5 L15.5 4 A10 10 0 0 1 24 12.5 Z" fill="#111"/></svg></div>
    <div class="icon-box" style="left:331px;top:70px"><svg width="28" height="28" viewBox="0 0 28 28" fill="none" stroke="#111" stroke-width="3"><circle cx="11" cy="11" r="8"/><line x1="17" y1="17" x2="26" y2="26"/></svg></div>
    <div class="vdiv" style="left:233px;top:88px;height:110px"></div>
    <div class="vdiv" style="left:316px;top:88px;height:110px"></div>
    <div class="subject" style="left:161px;top:124px"><h4>Subject</h4><p>Describe the first point here in a few short lines of supporting detail for the reader to review.</p></div>
    <div class="subject" style="left:241px;top:124px"><h4>Subject</h4><p>Describe the second point here in a few short lines of supporting detail for the reader to review.</p></div>
    <div class="subject" style="left:321px;top:124px"><h4>Subject</h4><p>Describe the third point here in a few short lines of supporting detail for the reader to review.</p></div>
    <footer class="footer"><span class="mark">HCP</span><span class="url">www.HaldenCapitalPartners.com</span><span class="page"><span>6</span></span></footer>
  </section>

  <!-- 7 Explanation, iconography & photo -->
  <section class="slide">
    <h2 class="title" style="left:36px;top:68px;font-size:14px;line-height:1.4">Explanation,<br>Iconography<br>&amp; Photo</h2>
    <div class="photo" style="left:142px;top:0;width:283px;height:214px;background:linear-gradient(100deg,#2d5c8a,#e6e2cf 40%,#3b4450 70%,#20262d)" role="img" aria-label="Photo of a high-rise office interior with city skyline through the windows"></div>
    <div class="icon-box" style="left:296px;top:8px"><svg width="30" height="30" viewBox="0 0 30 30" fill="none" stroke="#111" stroke-width="2"><circle cx="15" cy="15" r="13"/><polyline points="7,19 12,12 17,17 23,9"/></svg></div>
    <div class="icon-box" style="left:296px;top:84px"><svg width="28" height="28" viewBox="0 0 28 28" fill="none" stroke="#111" stroke-width="3"><circle cx="11" cy="11" r="8"/><line x1="17" y1="17" x2="26" y2="26"/></svg></div>
    <div class="icon-box" style="left:296px;top:158px"><svg width="28" height="28" viewBox="0 0 28 28"><circle cx="14" cy="14" r="12" fill="#111"/><path d="M15.5 12.5 L15.5 4 A10 10 0 0 1 24 12.5 Z" fill="var(--gold)"/></svg></div>
    <span class="num" style="left:345px;top:16px">01</span><p class="num-text" style="left:345px;top:32px">Short supporting note for the first point.</p>
    <span class="num" style="left:345px;top:90px">02</span><p class="num-text" style="left:349px;top:106px">Short supporting note for the second point.</p>
    <span class="num" style="left:345px;top:164px">03</span><p class="num-text" style="left:349px;top:180px">Short supporting note for the third point.</p>
    <footer class="footer"><span class="mark">HCP</span><span class="url">www.HaldenCapitalPartners.com</span><span class="page"><span>7</span></span></footer>
  </section>

  <!-- 8 Mission statement -->
  <section class="slide">
    <h2 class="title" style="left:24px;top:30px;font-size:14px">Mission Statement</h2>
    <div class="photo" style="left:24px;top:48px;width:387px;height:92px;background:linear-gradient(180deg,#a8b8d0,#7a7f98 50%,#3a2f3a 80%,#5c4a34)" role="img" aria-label="Photo of a city skyline at dusk with lit buildings along the water"></div>
    <div style="position:absolute;left:24px;top:140px;width:387px;height:58px;background:var(--gold);padding:8px 16px;font-size:7.8px;line-height:1.4;color:#1a1a1a">We advise a select group of private clients on the purchase of premium properties. Our mission is to offer clear analysis, honest counsel and lasting value on every transaction we handle, from first viewing to final close and well beyond.</div>
    <footer class="footer"><span class="mark">HCP</span><span class="url">www.HaldenCapitalPartners.com</span><span class="page"><span>8</span></span></footer>
  </section>

  <!-- 9 Contact -->
  <section class="slide dark">
    <div class="dark-bg" role="img" aria-label="Black and white photo of a dense downtown skyline"></div>
    <div class="dark-panel" style="left:26px;width:171px"></div>
    <h2 class="title" style="left:36px;top:26px;font-size:18px">Contact Us</h2>
    <div class="contact-row" style="top:70px"><span class="ic"><svg width="10" height="10" viewBox="0 0 24 24" fill="#111"><path d="M6.6 10.8a15 15 0 0 0 6.6 6.6l2.2-2.2a1 1 0 0 1 1-.25 11.4 11.4 0 0 0 3.6.57 1 1 0 0 1 1 1V20a1 1 0 0 1-1 1A17 17 0 0 1 3 4a1 1 0 0 1 1-1h3.5a1 1 0 0 1 1 1 11.4 11.4 0 0 0 .57 3.6 1 1 0 0 1-.25 1z"/></svg></span>415.555.0182</div>
    <div class="contact-row" style="top:99px"><span class="ic"><svg width="10" height="10" viewBox="0 0 24 24" fill="none" stroke="#111" stroke-width="2.4"><rect x="2" y="5" width="20" height="14"/><polyline points="2,5 12,13 22,5"/></svg></span>info@HaldenCapitalPartners.com</div>
    <div class="contact-row" style="top:127px"><span class="ic"><svg width="10" height="10" viewBox="0 0 24 24" fill="none" stroke="#111" stroke-width="2.2"><circle cx="12" cy="12" r="10"/><ellipse cx="12" cy="12" rx="4" ry="10"/><line x1="2" y1="12" x2="22" y2="12"/></svg></span>www.HaldenCapitalPartners.com</div>
    <div class="contact-row" style="top:155px"><span class="ic"><svg width="10" height="10" viewBox="0 0 24 24" fill="#111"><path d="M12 2a7 7 0 0 0-7 7c0 5 7 13 7 13s7-8 7-13a7 7 0 0 0-7-7zm0 9.5A2.5 2.5 0 1 1 12 6.5a2.5 2.5 0 0 1 0 5z"/></svg></span>48 Harbor Lane<br>Portland, OR 97201</div>
    <footer class="footer"><span class="mark">HCP</span><span class="url">www.HaldenCapitalPartners.com</span><span class="page"><span>9</span></span></footer>
  </section>

  <!-- 10 Legal -->
  <section class="slide dark">
    <div class="dark-bg" role="img" aria-label="Black and white photo of a downtown skyline with a tall tower"></div>
    <div class="dark-panel" style="left:26px;width:374px"></div>
    <h2 class="title" style="left:36px;top:26px;font-size:18px">Legal Disclaimer</h2>
    <div class="legal" style="position:absolute;left:36px;top:56px;width:356px">
      <p>This document is confidential and has been prepared solely for the named recipient. It may not be copied, shared or distributed to any other party without prior written consent.</p>
      <p>Information herein is drawn from sources believed to be reliable but is not guaranteed. Figures, projections and descriptions are provided for discussion only and should be independently verified by the recipient and its advisors.</p>
      <p>Nothing in this document constitutes an offer to sell.</p>
      <p>All square footage, income and expense figures are approximate and subject to change without notice at any time.</p>
      <p>Prospective buyers should consult their own legal, tax and financial advisors. Past performance of any property or market is not a reliable indicator of future results or returns on investment.</p>
      <p>Any site visit must be arranged in advance through our office.</p>
    </div>
    <footer class="footer"><span class="mark">HCP</span><span class="url">www.HaldenCapitalPartners.com</span><span class="page"><span>10</span></span></footer>
  </section>

</main>
</body>
</html>
```